Copperleaf Motorized Shade Business Card

Hello, we've had our logo made. Now we are looking for a clean and cool looking business card. One side can just be the logo with any design elements that might look good with it. The other side will be Name, Phone Number and Email. There will not be an address on the card.

```html
<!DOCTYPE html>
<html lang="en">
<head>
<meta charset="utf-8">
<title>Copperleaf Motorized Shade – Business Card</title>
<link rel="stylesheet" href="https://fonts.googleapis.com/css2?family=Source+Sans+3:wght@400;600;700;800&display=swap">
<style>
  :root {
    --backdrop: #f2bf2e;
    --card-dark: #3b3b3b;
    --card-dark-edge: #333333;
    --panel: #ececec;
    --navy: #143a78;
    --sky: #1a9ddc;
    --gold: #e8a915;
    --ink: #333333;
  }
  * { margin: 0; padding: 0; box-sizing: border-box; }
  html, body {
    width: 1183px; height: 1200px; overflow: hidden;
    background: var(--backdrop);
    font-family: "Source Sans 3", "Myriad Pro", sans-serif;
  }
  .sheet {
    width: 1183px; height: 1200px;
    display: flex; flex-direction: column; align-items: center;
    justify-content: center; gap: 24px;
  }
  .card {
    position: relative;
    width: 880px; height: 568px;
    background: linear-gradient(180deg, var(--card-dark) 0%, var(--card-dark-edge) 100%);
    overflow: hidden;
  }
  .card__panel {
    position: absolute;
    left: 231px; top: 0;
    width: 416px; height: 340px;
    background: var(--panel);
    box-shadow: 0 10px 18px rgba(0,0,0,0.55);
  }
  /* Front */
  .brand {
    position: absolute; inset: 0;
    display: flex; flex-direction: column; align-items: center; justify-content: center;
    color: var(--navy); font-weight: 700; text-align: center;
  }
  .brand__dot {
    width: 34px; height: 34px; border-radius: 50%;
    background: var(--gold); margin-bottom: 14px;
  }
  .brand__name { font-size: 64px; line-height: 1; letter-spacing: -0.5px; }
  .brand__tagline {
    font-size: 17px; letter-spacing: 5.5px; text-transform: uppercase; margin-top: 12px;
  }
  /* Back */
  .contact { position: absolute; left: 72px; top: 78px; }
  .contact__name { font-size: 32px; color: var(--navy); line-height: 1; letter-spacing: 0.5px; }
  .contact__name b { font-weight: 800; }
  .contact__name span { font-weight: 400; }
  .contact__role { font-size: 18px; color: var(--gold); margin-top: 6px; }
  .contact__list { list-style: none; margin-top: 26px; }
  .contact__item {
    display: flex; align-items: center; gap: 16px;
    font-size: 19px; color: var(--ink); height: 44px; letter-spacing: 0.3px;
  }
  .contact__icon { width: 36px; height: 36px; flex: none; }
</style>
</head>
<body>
<main class="sheet">
  <section class="card card--front" aria-label="Business card front">
    <div class="card__panel">
      <div class="brand">
        <div class="brand__dot"></div>
        <div class="brand__name">Copperleaf</div>
        <div class="brand__tagline">Motorized Shade</div>
      </div>
    </div>
  </section>

  <section class="card card--back" aria-label="Business card back">
    <div class="card__panel">
      <div class="contact">
        <h1 class="contact__name"><b>DARA</b> <span>VENN</span></h1>
        <p class="contact__role">sales manager</p>
        <ul class="contact__list">
          <li class="contact__item">
            <svg class="contact__icon" viewBox="0 0 36 36" aria-hidden="true">
              <circle cx="18" cy="18" r="18" fill="var(--sky)"/>
              <rect x="9" y="12" width="18" height="12" fill="none" stroke="#fff" stroke-width="1.8"/>
              <path d="M9 12 L18 19 L27 12 M9 24 L15.5 17.5 M27 24 L20.5 17.5" fill="none" stroke="#fff" stroke-width="1.6"/>
            </svg>
            dara.venn@copperleafshade.com
          </li>
          <li class="contact__item">
            <svg class="contact__icon" viewBox="0 0 36 36" aria-hidden="true">
              <circle cx="18" cy="18" r="18" fill="var(--sky)"/>
              <g fill="none" stroke="#fff" stroke-width="1.6">
                <circle cx="18" cy="18" r="9"/>
                <ellipse cx="18" cy="18" rx="4" ry="9"/>
                <path d="M9 18 H27 M10.5 13.5 H25.5 M10.5 22.5 H25.5"/>
              </g>
            </svg>
            www.copperleafshade.com
          </li>
          <li class="contact__item">
            <svg class="contact__icon" viewBox="0 0 36 36" aria-hidden="true">
              <circle cx="18" cy="18" r="18" fill="var(--sky)"/>
              <path d="M8 15 Q18 7 28 15 L25.5 18 L22 16 L22 13.5 Q18 12 14 13.5 L14 16 L10.5 18 Z" fill="#fff"/>
              <path d="M12 19 H24 L26 26 H10 Z" fill="#fff"/>
              <circle cx="18" cy="22.5" r="2" fill="var(--sky)"/>
            </svg>
            0055 41206837
          </li>
        </ul>
      </div>
    </div>
  </section>
</main>
</body>
</html>
```